Elegant and Professional Business card design needed

The patron journey mentor is a company which provides consulting services to businesses to assist them in improving the customer experience for their customers.

I need a business card design which tells people I'm there to help them.

Target Market(s)

Small to medium business owners

Industry/Entity Type

Business

Contact Information for Business Card

Martin Glenholme
The Patron Journey Mentor
Web: http://www.ThePatronJourneyMentor.example
Email: martin@ThePatronJourneyMentor.example
Phone: +61 400 582316

Logo styles of interest
Abstract Logo
Requirements
Must have
• Some sort of image / graphic representing the customer is important and should be at the heart of a business.

```html
<!DOCTYPE html>
<html lang="en">
<head>
<meta charset="utf-8">
<title>Martin Glenholme – Business Card</title>
<link href="https://fonts.googleapis.com/css2?family=Questrial&display=swap" rel="stylesheet">
<style>
  :root {
    --page-bg: #e9e7ea;
    --card-base: #a71f86;
    --card-edge: #8e1572;
    --card-glow: #df3fae;
    --band: rgba(88, 0, 66, 0.38);
    --text-light: #fbeef8;
    --text-soft: #f3d3ea;
    --tablet-frame: #f4f4f4;
    --tablet-screen: #dedede;
  }
  * { margin: 0; padding: 0; box-sizing: border-box; }
  html, body {
    width: 1200px; height: 874px; overflow: hidden;
    background: var(--page-bg);
  }
  .canvas {
    position: relative; width: 1200px; height: 874px;
    display: flex; align-items: center; justify-content: center;
  }
  .business-card {
    position: relative; width: 1000px; height: 571px;
    overflow: hidden; border-radius: 4px;
    background:
      radial-gradient(ellipse 60% 70% at 48% 42%, var(--card-glow) 0%, rgba(223,63,174,0) 70%),
      linear-gradient(135deg, var(--card-base) 0%, var(--card-edge) 100%);
    box-shadow: 0 14px 40px rgba(40, 0, 30, 0.25);
    font-family: "Questrial", "Century Gothic", sans-serif;
    color: var(--text-light);
  }
  .card-name {
    position: absolute; left: 80px; top: 150px;
    font-size: 60px; font-weight: 400; letter-spacing: 0.5px; line-height: 1;
    white-space: nowrap;
    text-shadow: 0 0 8px rgba(255, 255, 255, 0.45);
  }
  .card-title {
    position: absolute; left: 84px; top: 222px;
    font-size: 29px; letter-spacing: 2px; color: var(--text-soft);
    white-space: nowrap;
  }
  .contact-band {
    position: absolute; left: 110px; top: 290px;
    width: 520px; height: 144px;
    background: var(--band);
    padding: 20px 0 0 22px;
  }
  .contact-row {
    display: flex; align-items: center; gap: 14px;
    font-size: 22px; height: 36px; color: var(--text-light);
    white-space: nowrap;
  }
  .contact-row svg { width: 22px; height: 22px; flex: none; }
  .feedback-tablet {
    position: absolute; left: 640px; top: 70px;
    width: 290px; height: 200px; border-radius: 12px;
    background: var(--tablet-frame);
    box-shadow: 0 4px 12px rgba(50, 0, 40, 0.35);
    padding: 16px 20px 24px;
  }
  .feedback-tablet .screen {
    width: 100%; height: 100%;
    background: linear-gradient(180deg, #ffffff 0%, var(--tablet-screen) 100%);
    border: 1px solid #c9c9c9;
  }
</style>
</head>
<body>
<main class="canvas">
  <section class="business-card" aria-label="Business card for Martin Glenholme">
    <div class="feedback-tablet" role="img" aria-label="Tablet showing a customer rating checklist from Excellent to Poor, with Excellent ticked">
      <div class="screen"></div>
    </div>

    <h1 class="card-name">Martin Glenholme</h1>
    <p class="card-title">The Patron Journey Mentor</p>

    <div class="contact-band">
      <p class="contact-row">
        <svg viewBox="0 0 24 24" aria-hidden="true"><circle cx="12" cy="12" r="9" fill="none" stroke="currentColor" stroke-width="1.8"/><path d="M3 12h18M12 3c3 3 3 15 0 18M12 3c-3 3-3 15 0 18" fill="none" stroke="currentColor" stroke-width="1.5"/></svg>
        www.thepatronjourneymentor.example
      </p>
      <p class="contact-row">
        <svg viewBox="0 0 24 24" aria-hidden="true"><rect x="3" y="6" width="18" height="12" fill="none" stroke="currentColor" stroke-width="1.8"/><path d="M3 6l9 7 9-7" fill="none" stroke="currentColor" stroke-width="1.8"/></svg>
        martin@thepatronjourneymentor.example
      </p>
      <p class="contact-row">
        <svg viewBox="0 0 24 24" aria-hidden="true"><rect x="7" y="2.5" width="10" height="19" rx="2" fill="none" stroke="currentColor" stroke-width="1.8"/><circle cx="12" cy="18" r="1.2" fill="currentColor"/></svg>
        +61 400 582316
      </p>
    </div>
  </section>
</main>
</body>
</html>
```